Vegan bakery needs business card

We need a business card design for my vegan bakery in Philadelphia Pa. We create amazing whole food plant based cuisine that is egg and dairy free. We use fruits, vegetables, healing herbs, nuts, natural sugars (date, turbinado, agave) and non bleached flours in our creations. Due to demand and interest in the Philadelphia area we created a late night vegan dessert delivery service named Moonlark Greens. We are the only business providing delicious vegan desserts delivered to your door at 1am!! We would like to see designs that use the color scheme in the logo. The final design should communicate the benefits of our products: dairy/egg free, plant based, healing herbs, amazing food.

Industry/Entity Type

Business

```html
<!DOCTYPE html>
<html lang="en">
<head>
<meta charset="utf-8">
<title>Moonlark Greens – Business Card</title>
<link rel="stylesheet" href="https://fonts.googleapis.com/css2?family=Barlow:wght@500;600&family=Itim&display=swap">
<style>
  :root {
    --canvas: #ece8e3;
    --card-white: #ffffff;
    --card-brown: #4a2c25;
    --coral: #e0674f;
    --ink: #3a2420;
    --cream: #ffffff;
  }
  * { box-sizing: border-box; margin: 0; padding: 0; }
  html, body { width: 793px; height: 1200px; overflow: hidden; }
  body {
    background: var(--canvas);
    font-family: "Barlow", Arial, sans-serif;
    position: relative;
  }
  .card {
    position: absolute;
    top: 303px;
    width: 340px;
    height: 594px;
    border-radius: 18px;
    display: flex;
    flex-direction: column;
    align-items: center;
    box-shadow: 0 6px 18px rgba(0,0,0,0.12);
  }
  .card--front { left: 36px; background: var(--card-white); }
  .card--back { left: 417px; background: var(--card-brown); }

  .brand-name {
    margin-top: 92px;
    font-weight: 600;
    font-size: 38px;
    letter-spacing: 0.5px;
    color: var(--coral);
    text-align: center;
  }
  .card--back .brand-name { color: var(--cream); margin-top: 150px; }
  .brand-dot {
    margin-top: 18px;
    width: 96px;
    height: 96px;
    border-radius: 50%;
    background: var(--coral);
  }
  .contact {
    margin-top: 78px;
    text-align: center;
    color: var(--ink);
    font-weight: 600;
    font-size: 14px;
    line-height: 1.35;
    letter-spacing: 0.3px;
  }
  .contact__block + .contact__block { margin-top: 22px; }
  .social {
    margin-top: 38px;
    display: flex;
    gap: 12px;
  }
  .social__dot {
    width: 24px;
    height: 24px;
    border-radius: 50%;
    background: var(--coral);
  }
  .tagline {
    margin-top: 16px;
    font-family: "Itim", "Comic Sans MS", cursive;
    font-size: 25px;
    line-height: 1.1;
    color: var(--cream);
    text-align: center;
  }
</style>
</head>
<body>
  <section class="card card--front" aria-label="Business card front">
    <div class="brand-name">Moonlark Greens</div>
    <div class="brand-dot" aria-hidden="true"></div>
    <div class="contact">
      <div class="contact__block">
        <p>Moonlark Greens</p>
        <p>Pennsylvania, USA</p>
      </div>
      <div class="contact__block">
        <p>+ 01 267 555 0148</p>
        <p>info@moonlarkgreens.com</p>
        <p>www.moonlarkgreens.com</p>
      </div>
    </div>
    <div class="social" aria-label="Social media">
      <span class="social__dot"></span>
      <span class="social__dot"></span>
      <span class="social__dot"></span>
    </div>
  </section>

  <section class="card card--back" aria-label="Business card back">
    <div class="brand-name">Moonlark Greens</div>
    <div class="brand-dot" aria-hidden="true"></div>
    <p class="tagline">100% vegan<br>100% delicious</p>
  </section>
</body>
</html>
```